New Brochure Design Project

Need a product brochure for a Laboratory Informatics Company. Need something that is modern and very visually appealing, easy to read fonts and graphics. Preference is to use colors from our company logo colors.
We provide laboratory informatics software for the industries mentioned in the industries section. We work in the LIMS (Laboratory Information Management System) space.
We need an 8 Page brochure (12 pages if we can get creative to spread the content we have including application screen captures). Current brochure(VeriTab-General-2013-8P.pdf) is attached. Also attached in a zip file are several screen prints from the product. Any redundant sentences and any sentences that can be reworded or eliminated can be done. Please feel free to suggest.
Since our company name does not immediately indicate the product or product category we sell, we would like to add the following around (either on top or bottom) – LIMS | QMS | ELN | SDMS. Need not be exactly as shown here, but the 4 different applications need to stand out, around the company logo.
We would like to use good quality images to represent a laboratory, laboratory testing, laboratory instrument and processes, basically to get the feeling for laboratory or the LIMS industry. The front page (cover page) can list the industries we serve.
Graphics in the current brochure were done in Visio / PowerPoint several years ago and a modern graphic illustrating the same should be developed.
The product logos, company logos are also provided in the accompanying .zip file for reference. Use the product logos to give a visual of the products we offer.
Please let us know if you have any questions or need clarifications.
From the current brochure –
We do not want to use “All-in-one-LIMS etc….”
The last line LIMS->ELN->…. Should be removed!

Industry/Entity Type

Laboratory

Font styles to use
Serif
Sans Serif

Requirements
Must have
• page size will be 8.5 X 11
• fonts have to be professional and nice to read, stay with standard ones
• Prefer White of light bluish-grey back ground. Choose what ever looks nice, avoid any dark looking backgrounds. Should be color blind friendly.
Nice to have
• Good images for the product industry - LIMS - Laboratory Information Management System.
• Search for LIMS and you will be able to read what this industry is about and be able to design the brochure appropriately.
Should not have
• old look and feel, fonts

```html
<!DOCTYPE html>
<html lang="en">
<head>
<meta charset="utf-8">
<title>VeriTab – Product Highlights</title>
<link rel="stylesheet" href="https://fonts.googleapis.com/css2?family=Montserrat:wght@700;800&family=Tinos:wght@400;700&display=swap">
<style>
  :root {
    --blue-deep: #3f86c6;
    --blue-mid: #5da4d8;
    --blue-light: #9fcdec;
    --brand-blue: #1d5fa6;
    --heading-red: #c8161d;
    --body-ink: #3a3a3a;
    --paper: #ffffff;
    --photo-peach: #f3d9bf;
    --photo-teal: #bfe0e3;
  }
  * { margin: 0; padding: 0; box-sizing: border-box; }
  html, body { width: 849px; height: 1200px; overflow: hidden; background: var(--paper); }
  .page { position: relative; width: 849px; height: 1200px; overflow: hidden; background: var(--paper); }

  .header-band {
    position: absolute; left: 0; top: 0; width: 849px; height: 242px;
    background: linear-gradient(160deg, var(--blue-light) 0%, var(--blue-mid) 45%, var(--blue-deep) 100%);
  }
  .title { position: absolute; left: 48px; top: 142px; color: var(--paper); font-family: "Montserrat", sans-serif; }
  .title-main { display: block; font-size: 50px; font-weight: 800; line-height: 52px; letter-spacing: 0.5px; }
  .title-sub { display: block; font-size: 21px; font-weight: 700; line-height: 22px; margin-top: -2px; }
  .title-rule { position: absolute; left: 228px; top: 211px; width: 572px; height: 1px; background: var(--paper); }

  .lab-photo {
    position: absolute; left: 0; top: 860px; width: 849px; height: 340px;
    background:
      radial-gradient(ellipse 420px 220px at 280px 230px, rgba(191,224,227,0.75), rgba(191,224,227,0) 70%),
      radial-gradient(ellipse 500px 260px at 700px 260px, rgba(243,217,191,0.9), rgba(243,217,191,0) 75%),
      linear-gradient(180deg, rgba(255,255,255,1) 0%, rgba(248,236,224,1) 45%, var(--photo-peach) 100%);
  }

  .feature { position: absolute; width: 360px; font-family: "Tinos", serif; }
  .feature h2 { font-size: 17px; font-weight: 700; color: var(--heading-red); line-height: 24px; margin-bottom: 1px; }
  .feature p { font-size: 16.5px; color: var(--body-ink); line-height: 24px; }
  .col-left { left: 48px; }
  .col-right { left: 447px; }

  .brand { position: absolute; left: 540px; top: 1036px; width: 270px; height: 120px; }
  .brand-mark { position: absolute; left: 100px; top: 0; width: 66px; height: 66px; border-radius: 50%; background: var(--brand-blue); }
  .brand-name { position: absolute; left: 0; top: 86px; width: 270px; text-align: right;
    font-family: "Montserrat", sans-serif; font-weight: 700; font-size: 22px; color: var(--brand-blue); }
</style>
</head>
<body>
<div class="page">
  <div class="header-band" role="img" aria-label="Faceted low-poly pattern in shades of light and mid blue"></div>
  <h1 class="title"><span class="title-main">Product</span><span class="title-sub">Highlights</span></h1>
  <div class="title-rule"></div>

  <div class="lab-photo" role="img" aria-label="Faded photograph of gloved hands holding a labelled sample tube in a laboratory"></div>

  <section class="feature col-left" style="top:291px">
    <h2>Configurability</h2>
    <p>Easy configuration to adapt to lab specific requirements. Easy definition of business logic and workflow management.</p>
  </section>
  <section class="feature col-left" style="top:411px">
    <h2>Extensibility</h2>
    <p>Easy to accommodate new requirements. Extend user interface, business logic and database model without programming (using VeriTab Studio)</p>
  </section>
  <section class="feature col-left" style="top:556px">
    <h2>Upgradability</h2>
    <p>Configuration and extended functionality are retained through product upgrades.</p>
  </section>
  <section class="feature col-left" style="top:652px">
    <h2>External System Integration</h2>
    <p>Can be integrated with a variety of external systems such as ERP, CDS etc… using pre-built connectors and web service.</p>
  </section>
  <section class="feature col-left" style="top:773px">
    <h2>Instrument Integration</h2>
    <p>Ready for integration with a range of instruments and systems via configuration without any programming (No coding required) by using built-in framework.</p>
  </section>

  <section class="feature col-right" style="top:291px">
    <h2>Reporting</h2>
    <p>Supports Prism Reports and Opal Reports for reporting.</p>
  </section>
  <section class="feature col-right" style="top:387px">
    <h2>Ad-hoc Query</h2>
    <p>Built in capability to query the database using a query builder tool.</p>
  </section>
  <section class="feature col-right" style="top:484px">
    <h2>Dashboard</h2>
    <p>Built in dashboards, personalized by users/ roles and extensible via configuration.</p>
  </section>
  <section class="feature col-right" style="top:580px">
    <h2>Barcoding</h2>
    <p>Supports barcode label printing and scanning.</p>
  </section>
  <section class="feature col-right" style="top:652px">
    <h2>Scheduling</h2>
    <p>Easy to schedule events and user alerts.</p>
  </section>
  <section class="feature col-right" style="top:725px">
    <h2>Security</h2>
    <p>Granular security specification for user access control based on roles. Integrates with Central Directory for user authentication.</p>
  </section>

  <div class="brand">
    <div class="brand-mark"></div>
    <div class="brand-name">Veranth Systems</div>
  </div>
</div>
</body>
</html>
```